Business Card and Stationery for Construction/Restoration/Cleaning Company
Logo attached; Slogan: One Call Restores It All; Fire, Water, Storm, Mold
Business Card and Stationery for Construction/Restoration/Cleaning Company - Construction
Creative Brief
Use same font as used in my logo
Dale Morrow
Project Manager/Estimator
4182 Tindall Street, Suite B Portage, Indiana 40713
dale@brvxnorthern.com
www.brvxnorthern.com
OPTWA Registration Number
Slogan: One Call Restores It All Fire, Water, Storm, Mold If possible, We would like to try and have this on the front of the card somewhere.
24/7 - uploaded OPTWA Logo - uploaded Full Service Disaster Restoration: Board up Services Fire and Smoke Damage Water Remediation Mold Remediation Storm Damage Content Cleaning Content Pack Out Reconstruction Services Construction Services: Demolition New Construction Commercial Build-out Addition/Remodel Improvement/Repairs
workaholicdrw workaholicdrw
Further clarification for everyone. The OPTWA Registration is tied to the individual not the company. If it will fit well in the design, we were looking to have the tag line: "One Call Restores it All" on the front with the "Fire, Water, Storm and Mold". It would be nice if this could be on the stationery also. On the stationery, we do need the individual's name or phone numbers, or OPTWA Registration Number. Just the company information.
I need to correct something on my brief. 1) Please add our Toll Free number 844-731-6208 to front of card. 2) On the front of the card, please add 372948 after OPTWA Registration Number. Any questions, please let me know. Thank you. kmt

```html
<!DOCTYPE html>
<html lang="en">
<head>
<meta charset="utf-8">
<title>Corvane Restoration – Stationery</title>
<link href="https://fonts.googleapis.com/css2?family=Montserrat:wght@400;600;700&display=swap" rel="stylesheet">
<style>
  :root{
    --bg:#6e6e6e;
    --paper:#ffffff;
    --blue:#1f78c4;
    --blue-deep:#0c3f74;
    --navy:#0a2c52;
    --ink:#2b3440;
    --rule:#c9d3de;
  }
  *{box-sizing:border-box;margin:0;padding:0}
  html,body{width:1200px;height:204px;overflow:hidden;background:var(--bg);font-family:"Montserrat",sans-serif;color:var(--ink)}
  .stage{position:relative;width:1200px;height:204px}
  .piece{position:absolute;background:var(--paper);box-shadow:0 2px 5px rgba(0,0,0,.35);overflow:hidden}
  .blue{background:linear-gradient(135deg,var(--blue) 0%,var(--blue-deep) 70%,var(--navy) 100%)}
  .brand{display:flex;align-items:center;gap:3px;font-weight:700;color:var(--blue-deep);white-space:nowrap;line-height:1}
  .brand .dot{border-radius:50%;background:var(--blue);flex:none}
  .brand.light{color:#fff}
  .brand.light .dot{background:#fff}
  .tiny{font-size:2.8px;line-height:1.4;white-space:nowrap}
  .swoosh{position:absolute;left:0;bottom:0;width:100%;height:100%}
  .bars span{display:block;height:1.2px;background:var(--rule);margin-bottom:2.6px}

  /* business cards */
  .card{width:80px;height:44px}
  .card-front-a{left:12px;top:104px}
  .card-back-a{left:98px;top:104px}
  .card-front-b{left:12px;top:154px}
  .card-back-b{left:98px;top:154px}
  .card-front .brand{position:absolute;left:5px;top:5px;font-size:4.4px}
  .card-front .brand .dot{width:5px;height:5px}
  .card-front .who{position:absolute;right:5px;top:5px;text-align:right}
  .card-front .who b{font-size:3.4px;display:block;color:var(--blue-deep);margin-bottom:1px}
  .card-front .contact{position:absolute;left:5px;top:14px}
  .card-back .brand{position:absolute;left:50%;top:13px;transform:translateX(-50%);font-size:5.5px}
  .card-back .brand .dot{width:6px;height:6px}
  .card-back .slogan{position:absolute;width:100%;top:24px;text-align:center;color:#fff;font-size:2.8px}

  /* letterheads */
  .letter{top:22px;width:110px;height:160px}
  .letter-a{left:190px}
  .letter-b{left:310px}
  .letter .brand{position:absolute;left:8px;top:9px;font-size:5px}
  .letter .brand .dot{width:6px;height:6px}
  .letter .head-info{position:absolute;right:8px;top:8px;text-align:right}
  .letter .bars{position:absolute;left:12px;right:12px;top:34px}
  .letter .foot{position:absolute;left:0;bottom:0;width:100%;height:14px}
  .letter .foot .tiny{position:absolute;left:8px;top:5px;color:#fff}

  /* compliment slip */
  .slip{left:442px;top:40px;width:128px;height:42px}
  .slip .brand{position:absolute;left:7px;top:7px;font-size:5px}
  .slip .brand .dot{width:6px;height:6px}
  .slip .bars{position:absolute;left:7px;right:36px;top:20px}
  .slip .side{position:absolute;right:0;top:0;width:26px;height:100%}

  /* envelopes */
  .env{left:434px;width:150px;height:48px}
  .env-a{top:92px}
  .env-b{top:146px}
  .env .brand{position:absolute;left:6px;top:6px;font-size:4.6px}
  .env .brand .dot{width:5px;height:5px}
  .env-b .flap{position:absolute;left:0;top:0;width:100%;height:20px}

  /* folder */
  .folder{left:612px;top:16px;width:204px;height:172px;background:none;box-shadow:none;display:flex;gap:2px;overflow:visible}
  .folder .panel{position:relative;flex:1;box-shadow:0 2px 5px rgba(0,0,0,.35);overflow:hidden}
  .folder .inside{background:var(--paper)}
  .folder .cover .brand{position:absolute;left:50%;top:62px;transform:translateX(-50%);font-size:6.5px}
  .folder .cover .brand .dot{width:8px;height:8px}
  .folder .cover .slogan{position:absolute;width:100%;top:78px;text-align:center;color:#fff;font-size:3.2px;line-height:1.4}
  .folder .pocket{position:absolute;left:0;bottom:0;width:100%;height:60px}

  /* disc */
  .disc{left:850px;top:40px;width:100px;height:100px;border-radius:50%}
  .disc .hole{position:absolute;left:50%;top:50%;width:22px;height:22px;margin:-11px 0 0 -11px;border-radius:50%;background:var(--bg);border:5px solid #dfe6ee}
  .disc .brand{position:absolute;left:50%;top:20px;transform:translateX(-50%);font-size:5px}
  .disc .brand .dot{width:6px;height:6px}

  /* disc sleeve */
  .sleeve{left:1076px;top:40px;width:104px;height:104px}
  .sleeve .window{position:absolute;left:50%;top:50%;width:56px;height:56px;margin:-28px 0 0 -28px;border-radius:50%;border:1px solid var(--rule)}
  .sleeve .brand{position:absolute;left:8px;top:8px;font-size:5px}
  .sleeve .brand .dot{width:6px;height:6px}
</style>
</head>
<body>
<main class="stage">

  <section class="piece card card-front card-front-a" aria-label="Business card front">
    <svg class="swoosh" viewBox="0 0 80 44" preserveAspectRatio="none" aria-hidden="true">
      <path d="M0 36 Q40 30 80 38 L80 44 L0 44Z" fill="#1f78c4"/>
      <path d="M0 40 Q40 35 80 41 L80 44 L0 44Z" fill="#0c3f74"/>
    </svg>
    <div class="brand"><span class="dot"></span>Corvane</div>
    <div class="who tiny"><b>Dale Morrow</b>Project Manager/Estimator<br>Toll Free 844-731-6208</div>
    <div class="contact tiny">4182 Tindall Street, Suite B<br>Portage, Indiana 40713<br>dale@brvxnorthern.com<br>OPTWA Reg. No. 372948</div>
  </section>

  <section class="piece card card-back card-back-a blue" aria-label="Business card back">
    <div class="brand light"><span class="dot"></span>Corvane</div>
    <p class="slogan">One Call Restores It All · Fire, Water, Storm, Mold</p>
  </section>

  <section class="piece card card-back card-back-b blue" aria-label="Business card back">
    <div class="brand light"><span class="dot"></span>Corvane</div>
    <p class="slogan">One Call Restores It All · Fire, Water, Storm, Mold</p>
  </section>

  <section class="piece card card-front card-front-b" aria-label="Business card front">
    <svg class="swoosh" viewBox="0 0 80 44" preserveAspectRatio="none" aria-hidden="true">
      <path d="M0 36 Q40 30 80 38 L80 44 L0 44Z" fill="#1f78c4"/>
      <path d="M0 40 Q40 35 80 41 L80 44 L0 44Z" fill="#0c3f74"/>
    </svg>
    <div class="brand"><span class="dot"></span>Corvane</div>
    <div class="who tiny"><b>Dale Morrow</b>Project Manager/Estimator<br>Toll Free 844-731-6208</div>
    <div class="contact tiny">4182 Tindall Street, Suite B<br>Portage, Indiana 40713<br>www.brvxnorthern.com<br>OPTWA Reg. No. 372948</div>
  </section>

  <section class="piece letter letter-a" aria-label="Letterhead">
    <div class="brand"><span class="dot"></span>Corvane</div>
    <div class="head-info tiny">4182 Tindall Street, Suite B<br>Portage, Indiana 40713<br>www.brvxnorthern.com</div>
    <div class="bars"><span></span><span></span><span></span><span></span><span></span><span></span><span style="width:70%"></span><span></span><span></span><span></span><span></span><span style="width:55%"></span><span></span><span></span><span></span><span style="width:40%"></span></div>
    <div class="foot blue"><p class="tiny">One Call Restores It All · Fire, Water, Storm, Mold</p></div>
  </section>

  <section class="piece letter letter-b" aria-label="Letterhead continuation">
    <div class="brand"><span class="dot"></span>Corvane</div>
    <div class="head-info tiny">4182 Tindall Street, Suite B<br>Portage, Indiana 40713<br>www.brvxnorthern.com</div>
    <div class="bars"><span></span><span></span><span></span><span></span><span style="width:80%"></span><span></span><span></span><span></span><span style="width:60%"></span><span></span><span></span><span></span><span></span><span style="width:45%"></span></div>
    <div class="foot blue"><p class="tiny">One Call Restores It All · Fire, Water, Storm, Mold</p></div>
  </section>

  <section class="piece slip" aria-label="Compliment slip">
    <div class="brand"><span class="dot"></span>Corvane</div>
    <div class="bars"><span></span><span></span><span style="width:60%"></span></div>
    <div class="side blue"></div>
  </section>

  <section class="piece env env-a" aria-label="Envelope front">
    <div class="brand"><span class="dot"></span>Corvane</div>
    <svg class="swoosh" viewBox="0 0 150 48" preserveAspectRatio="none" aria-hidden="true">
      <path d="M0 40 Q75 33 150 42 L150 48 L0 48Z" fill="#1f78c4"/>
    </svg>
  </section>

  <section class="piece env env-b" aria-label="Envelope back">
    <svg class="flap" viewBox="0 0 150 20" preserveAspectRatio="none" aria-hidden="true">
      <path d="M0 0 L150 0 L150 6 Q75 26 0 6Z" fill="#0c3f74"/>
    </svg>
  </section>

  <section class="piece folder" aria-label="Presentation folder">
    <div class="panel inside">
      <svg class="pocket" viewBox="0 0 101 60" preserveAspectRatio="none" aria-hidden="true">
        <path d="M0 14 Q50 0 101 10 L101 60 L0 60Z" fill="#1f78c4"/>
        <path d="M0 24 Q50 12 101 20 L101 60 L0 60Z" fill="#0c3f74"/>
      </svg>
    </div>
    <div class="panel cover blue">
      <div class="brand light"><span class="dot"></span>Corvane</div>
      <p class="slogan">One Call Restores It All<br>Fire, Water, Storm, Mold</p>
    </div>
  </section>

  <section class="piece disc blue" aria-label="Disc label">
    <div class="brand light"><span class="dot"></span>Corvane</div>
    <div class="hole"></div>
  </section>

  <section class="piece sleeve" aria-label="Disc sleeve">
    <div class="brand"><span class="dot"></span>Corvane</div>
    <div class="window"></div>
    <svg class="swoosh" viewBox="0 0 104 104" preserveAspectRatio="none" aria-hidden="true">
      <path d="M0 92 Q52 82 104 94 L104 104 L0 104Z" fill="#1f78c4"/>
    </svg>
  </section>

</main>
</body>
</html>
```